- Redesign our business card
- Logo remains unchanged
- Current business card attached

Target Market(s)

We are a property management company

Industry/Entity Type

Business

```html
<!DOCTYPE html>
<html lang="en">
<head>
<meta charset="utf-8">
<title>Kestrel Property Group – Business Card</title>
<link href="https://fonts.googleapis.com/css2?family=Roboto:wght@300;400;700&family=Roboto+Condensed:wght@700&display=swap" rel="stylesheet">
<style>
  :root {
    --stage: #000000;
    --paper: #ffffff;
    --olive: #858145;
    --beige: #dccfae;
    --slate: #5f5f62;
    --ink: #3a3a3a;
    --white: #ffffff;
  }
  html, body {
    margin: 0;
    padding: 0;
    width: 1200px;
    height: 900px;
    overflow: hidden;
    background: var(--stage);
    font-family: "Roboto", Arial, sans-serif;
  }
  .canvas {
    position: relative;
    width: 1200px;
    height: 900px;
  }
  .card {
    position: absolute;
    left: 244px;
    width: 662px;
    height: 380px;
    overflow: hidden;
  }
  .card--front { top: 44px; background: var(--paper); }
  .card--back  { top: 468px; background: var(--olive); }

  /* Front: brand lockup */
  .brand {
    position: absolute;
    left: 404px;
    top: 26px;
    width: 228px;
  }
  .brand__mark {
    display: block;
    width: 90px;
    height: 90px;
    margin-left: 6px;
    margin-bottom: 12px;
    background: var(--beige);
  }
  .brand__name {
    font-weight: 700;
    font-size: 16px;
    letter-spacing: 0.4px;
    color: var(--olive);
    line-height: 1;
    white-space: nowrap;
  }
  .brand__tagline {
    margin-top: 3px;
    font-weight: 400;
    font-size: 10px;
    letter-spacing: 1.2px;
    color: var(--slate);
    white-space: nowrap;
  }

  /* Front: person */
  .person {
    position: absolute;
    left: 24px;
    top: 194px;
  }
  .person__name {
    font-family: "Roboto Condensed", Arial, sans-serif;
    font-weight: 700;
    font-size: 20px;
    letter-spacing: 0.5px;
    color: var(--olive);
    line-height: 1;
  }
  .person__role {
    margin-top: 5px;
    font-weight: 400;
    font-size: 17px;
    color: var(--ink);
  }

  /* Front: contact band */
  .contact-band {
    position: absolute;
    left: 0;
    top: 256px;
    width: 100%;
    height: 104px;
    background: var(--olive);
    color: var(--white);
  }
  .contact-band__base {
    position: absolute;
    left: 0;
    top: 360px;
    width: 100%;
    height: 20px;
    background: var(--slate);
  }
  .contact {
    position: absolute;
    top: 24px;
    font-size: 12px;
    line-height: 17px;
  }
  .contact--address { left: 24px; width: 232px; font-weight: 700; }
  .contact--phones  { left: 292px; font-weight: 300; }
  .contact--online  { left: 440px; font-weight: 300; }
  .divider {
    position: absolute;
    top: 20px;
    width: 1px;
    height: 60px;
    background: var(--white);
  }
  .divider--one { left: 272px; }
  .divider--two { left: 416px; }

  /* Back */
  .back-brand {
    position: absolute;
    left: 0;
    top: 112px;
    width: 100%;
    text-align: center;
    color: var(--white);
  }
  .back-brand__mark {
    display: block;
    margin: 0 auto 8px;
    width: 36px;
    height: 36px;
    background: var(--white);
  }
  .back-brand__name {
    font-weight: 700;
    font-size: 11px;
    letter-spacing: 1.5px;
    line-height: 1;
  }
  .back-web {
    position: absolute;
    left: 0;
    top: 186px;
    width: 100%;
    text-align: center;
    font-weight: 300;
    font-size: 19px;
    letter-spacing: 3px;
    color: var(--white);
    line-height: 1.2;
  }
  .back-web strong { font-weight: 700; }
  .back-services {
    position: absolute;
    left: 0;
    top: 226px;
    width: 100%;
    text-align: center;
    font-weight: 300;
    font-size: 14px;
    color: var(--white);
  }
</style>
</head>
<body>
<div class="canvas">

  <section class="card card--front">
    <div class="brand">
      <span class="brand__mark"></span>
      <div class="brand__name">KESTREL PROPERTY GROUP</div>
      <div class="brand__tagline">STRATA MANAGEMENT SERVICES</div>
    </div>

    <div class="person">
      <div class="person__name">DANIEL MARSH</div>
      <div class="person__role">Licensed Strata Manager</div>
    </div>

    <div class="contact-band">
      <div class="contact contact--address">PO BOX 48, REDFERN VALE NSW 2016 12/3-9 MARLOW STREET REDFERN VALE NSW 2016</div>
      <span class="divider divider--one"></span>
      <div class="contact contact--phones">T: 02 9000 1260<br>F: 02 9000 1274<br>M: 0400 318 27</div>
      <span class="divider divider--two"></span>
      <div class="contact contact--online">E: info@kestrelproperty.com.au<br>www.kestrelproperty.com.au</div>
    </div>
    <div class="contact-band__base"></div>
  </section>

  <section class="card card--back">
    <div class="back-brand">
      <span class="back-brand__mark"></span>
      <div class="back-brand__name">KESTREL PROPERTY GROUP</div>
    </div>
    <div class="back-web">www.<strong>kestrelproperty</strong>.com.au</div>
    <div class="back-services">Strata Management | Community Management | Property Management</div>
  </section>

</div>
</body>
</html>
```